Jolie Plume Gourmet Brie Packaging

I developed and market a 10oz wheel (7inch dia) and a 6 oz wheel (5 inch dia) Gourmet Brie Cheese Line. They are all double cream bries, topped with decadent concoctions and wrapped with buttery puff pastry. They are frozen and vacuum sealed. They are sold in markets as a frozen item. I am looking for a paper "slip"/ wrap to house the brie that would have my logo, nutritional info, and cooking instructions in a mod fresh background. The company Name is Jolie Plume (bright spoon). and the Product if Gourmet Brie. I would like to wrapper to be able to house both sizes so I dont double my costs. My Logo for Jolie Plume is a Red sketched chicken in the middle of the name. The writing is in Black (le Carte pen is the font I used)
My website is brightspoon-events.example.
Updates

I have added a logo file for the packaging.  The logo should be the jolie plume chicken and not bright spoon events.  Also, I would like the style and colors to match with this  - THANKS!

I have updated to Jolie Plume Logo - Please make the change to your designs.  I will be selecting design a week from today.  The choosen design may require a few edits, but minimal. Thanks!

Reason: I will be choosing Design April 2. Please have any changes, designs and or ideas to Jolie Plume by then. Thanks you all so much for what you submitted....I like them all!!!!

Target Market(s)

Gourmet Food/Wine Shops /upscale grocery.

Industry/Entity Type

Cooking

Requirements
Must have
• Ingredients, Nutritional info, directions.
Logo and name.

```html
<!DOCTYPE html>
<html lang="en">
<head>
<meta charset="utf-8">
<title>Jolie Plume Gourmet Brie – Wrap Label</title>
<link rel="stylesheet" href="https://fonts.googleapis.com/css2?family=IM+Fell+English:ital@1&family=Meddon&family=Open+Sans:wght@400;800&display=swap">
<style>
  :root {
    --page: #ffffff;
    --label: #efefef;
    --frame: #4a4a4a;
    --ink: #1a1a1a;
    --script-red: #a3151a;
    --title-shadow: rgba(0, 0, 0, 0.4);
    --photo-edge: #9b1b1e;
  }
  html, body {
    margin: 0;
    width: 1200px;
    height: 900px;
    overflow: hidden;
    background: var(--page);
  }
  .canvas {
    position: relative;
    width: 1200px;
    height: 900px;
  }
  .label {
    position: absolute;
    left: 165px;
    top: 0;
    width: 853px;
    height: 895px;
    background: var(--label);
    border: 2px solid var(--frame);
  }
  .label-art {
    position: absolute;
    inset: 0;
    width: 1200px;
    height: 900px;
  }
  .ring-text, .ring-heading {
    font-family: "IM Fell English", serif;
    font-style: italic;
    fill: var(--script-red);
  }
  .ring-text { font-size: 19px; }
  .ring-heading { font-size: 21px; }
  .product-title {
    font-family: "Meddon", cursive;
    font-size: 104px;
    fill: var(--ink);
    filter: drop-shadow(6px 7px 4px var(--title-shadow));
  }
  .brand-name {
    position: absolute;
    left: 480px;
    top: 326px;
    width: 200px;
    text-align: center;
    font-family: "Open Sans", sans-serif;
    font-weight: 800;
    font-size: 30px;
    color: var(--ink);
    margin: 0;
    letter-spacing: 0.5px;
  }
  .storage-note {
    position: absolute;
    left: 752px;
    top: 588px;
    width: 170px;
    margin: 0;
    text-align: center;
    font-family: "Open Sans", sans-serif;
    font-size: 17px;
    line-height: 1.2;
    color: var(--ink);
    transform: rotate(-66deg);
    transform-origin: center;
  }
</style>
</head>
<body>
<main class="canvas">
  <section class="label"></section>

  <svg class="label-art" viewBox="0 0 1200 900" xmlns="http://www.w3.org/2000/svg">
    <defs>
      <path id="instruction-ring" d="M 791.5 124.5 A 395 395 0 1 1 465 99"/>
      <linearGradient id="brie-tones" x1="0" y1="0" x2="1" y2="1">
        <stop offset="0" stop-color="#3a2418"/>
        <stop offset="0.35" stop-color="#d9c49a"/>
        <stop offset="0.6" stop-color="#c9a86a"/>
        <stop offset="1" stop-color="#4a2a18"/>
      </linearGradient>
    </defs>

    <text class="ring-heading" x="603" y="45" transform="rotate(17 603 45)">Cooking Instruction:</text>
    <text class="ring-heading" x="680" y="92" transform="rotate(22 680 92)">Ingridients:</text>

    <text class="ring-text">
      <textPath href="#instruction-ring" textLength="2140" lengthAdjust="spacing">Remove the packaging and Thaw in Refrigerator overnight or on counter for two hours before Baking. Place on Baking pan, brush with a beaten egg and bake at 400 degrees for 25-35 minutes until pastry is Puffed and Golden. Let stand for 15 minutes Before serving.</textPath>
    </text>

    <rect class="product-photo" x="429" y="538" width="339" height="220" rx="110" ry="110"
          fill="url(#brie-tones)" stroke="var(--photo-edge)" stroke-width="2.5"
          role="img" aria-label="Photo of baked brie in golden puff pastry, sliced open with cranberry filling, pecans and raisins on a wooden board"/>

    <text class="product-title" x="285" y="498" textLength="640" lengthAdjust="spacingAndGlyphs">Gourmet Brie</text>
  </svg>

  <p class="brand-name">Jolie Plume</p>
  <p class="storage-note">Frozen &amp;<br>Vaccumed sealed<br>For Freshness.<br>Keep Frozen.</p>
</main>
</body>
</html>
```